KV Group

We need a new website for our company and since we had a very good work done for our logo in this site, we're back for the entire job.

Our company name is Marlowe Capital Group. We're adding files of examples of what we have done today. In my opinion we need a more attention lock in the site but yet financial simple work.

Our files (attached) will let you know what we have so far. We need a complete change but the colours should be the same, however you can change them not running away to far from the original, and of course matching with the logo.

We need examples for 3 kind of layouts.

- A HOME welcome layout
- An internal Layout with sidebar
- And internal Layout wide

We can buy image licenses if needed for assets.
Actually there are 5 slide images placed on the Welcome HOME, we need those there, but you can improve with better images to match the new website!!!

Target Market(s)

Clients looking for financial advisers, tax and funds specialist, currency advisers

Industry/Entity Type

Financial

Requirements
Must have
• all the fonts must be in accordance with the financial market sites........the welcome home page must be precise, neat and information accurate........the menu should be elegant........main focus on the Home page, should be also the PRIVATE ACCESS box log in.......

```html
<!DOCTYPE html>
<html lang="en">
<head>
<meta charset="utf-8">
<title>Marlowe Capital Group</title>
<link rel="stylesheet" href="https://fonts.googleapis.com/css2?family=Open+Sans:wght@400;600;700&family=Roboto:wght@400;500&display=swap">
<style>
:root{
  --orange:#d9680f;
  --orange-light:#f39042;
  --orange-dark:#a94b09;
  --brown:#3b2414;
  --brown-dark:#2a180c;
  --panel:#efece6;
  --text:#6b645c;
  --ticker:#f2f1ed;
  --footer:#444444;
  --footer-dark:#2b2b2b;
  --footer-bottom:#3a3a3a;
  --white:#ffffff;
}
*{box-sizing:border-box;margin:0;padding:0}
html,body{width:741px;height:1200px;overflow:hidden;background:var(--white)}
body{position:relative;font-family:"Open Sans",Arial,sans-serif;color:var(--text)}
.abs{position:absolute}

/* header */
.brand{left:80px;top:16px;width:140px;display:flex;align-items:center;gap:8px}
.brand-mark{width:26px;height:26px;background:var(--orange);flex:none}
.brand-name{font-size:13px;font-weight:700;color:var(--brown);line-height:1.15;letter-spacing:.3px}
.access{left:413px;top:7px;width:248px;height:68px;background:var(--orange);border-radius:2px}
.access h2{position:absolute;left:12px;top:6px;font:600 11px "Open Sans",sans-serif;color:var(--white);letter-spacing:.3px}
.access .field{position:absolute;top:23px;width:107px;height:17px;background:var(--white);border-radius:2px;font-size:7.5px;font-style:italic;color:#999;padding:3px 7px}
.access .forgot{position:absolute;left:95px;top:51px;font-size:7.5px;font-style:italic;color:var(--white)}
.access .login{position:absolute;left:193px;top:46px;width:44px;height:19px;background:var(--brown);border-radius:3px;color:var(--white);font-size:8px;font-weight:600;text-align:center;line-height:19px}

.nav{left:80px;top:83px;width:581px;height:28px;background:linear-gradient(var(--brown),var(--brown-dark));display:flex;justify-content:space-between;align-items:center;padding:0 14px}
.nav a{color:var(--white);font:500 8.5px "Roboto",sans-serif;text-decoration:none;letter-spacing:.2px}

/* hero */
.hero{left:0;top:111px;width:741px;height:224px;background:linear-gradient(var(--orange-light),#ee7f2b)}
.slide-side{position:absolute;top:25px;width:104px;height:147px}
.slide-left{left:80px;background:
  linear-gradient(180deg,rgba(255,255,255,0) 60%,rgba(160,190,60,.7) 100%),
  linear-gradient(120deg,#fbfbfa 0%,#e9ebe6 45%,#c9cfc0 70%,#8f9a84 100%)}
.slide-right{left:557px;background:
  radial-gradient(ellipse at 25% 20%,#f2f4f6 0%,#dfe4ea 25%,rgba(0,0,0,0) 45%),
  linear-gradient(110deg,#c9d1da 0%,#3a4664 40%,#1e2740 70%,#141a2b 100%)}
.slide-main{position:absolute;left:183px;top:15px;width:375px;height:167px;background:var(--white);padding:4px;box-shadow:0 2px 6px rgba(0,0,0,.35)}
.slide-photo{width:100%;height:100%;position:relative;background:
  radial-gradient(ellipse at 62% 55%,rgba(255,214,140,.55) 0%,rgba(255,190,110,.25) 25%,rgba(0,0,0,0) 55%),
  radial-gradient(ellipse at 30% 70%,rgba(255,200,120,.35) 0%,rgba(0,0,0,0) 40%),
  linear-gradient(#8a8790 0%,#6b6870 30%,#45404a 55%,#2e2922 80%,#1d1812 100%)}
.caption{position:absolute;left:0;bottom:0;width:100%;height:49px;background:rgba(20,20,20,.78);padding:5px 10px;color:var(--white)}
.caption h3{font:500 12.5px "Roboto",sans-serif;letter-spacing:.4px}
.caption p{font-size:9px;line-height:11px;margin-top:3px}
.arrows{position:absolute;top:196px;left:347px;display:flex;gap:6px}

/* ticker */
.ticker{left:0;top:338px;width:741px;height:27px;background:var(--ticker);border-top:1px solid #ddd;border-bottom:1px solid #ddd;font:700 7px "Open Sans",sans-serif;color:var(--brown);white-space:nowrap;overflow:hidden;padding-top:8px}
.ticker span{margin-right:16px}
.up{color:#2c8c2c}.down{color:#d11}.flat{color:#d99a00}

/* sections */
.section{left:80px;width:581px;height:168px;background:var(--panel)}
.section-head{height:25px;background:linear-gradient(#c9620f,var(--orange-dark));position:relative}
.section-head h2{position:absolute;top:4px;font:500 13px "Roboto",sans-serif;color:var(--white)}
.section-head .pointer{position:absolute;top:25px;width:0;height:0;border-left:15px solid transparent;border-right:15px solid transparent;border-top:12px solid var(--orange-dark)}
.section p{position:absolute;width:322px;font-size:7.6px;line-height:14.2px;color:var(--text)}
.section .more{position:absolute;font-size:7.6px;font-weight:600;color:var(--brown)}
.frame{position:absolute;background:var(--white);padding:4px;box-shadow:0 1px 3px rgba(0,0,0,.2)}
.frame div{width:100%;height:100%}
.img-charts{background:
  linear-gradient(180deg,rgba(255,255,255,0) 62%,rgba(150,200,40,.55) 78%,rgba(90,180,200,.45) 100%),
  linear-gradient(125deg,#f8f8f6 0%,#e6e7e2 45%,#d6d8d0 65%,#b8bcb0 100%)}
.img-market{background:
  radial-gradient(ellipse at 30% 65%,rgba(170,215,250,.7) 0%,rgba(0,0,0,0) 40%),
  radial-gradient(ellipse at 80% 25%,rgba(230,240,255,.5) 0%,rgba(0,0,0,0) 35%),
  linear-gradient(135deg,#6fb0e6 0%,#3a8ad6 40%,#1f62b8 70%,#0f3d88 100%)}
.img-trade{background:
  linear-gradient(180deg,rgba(0,0,0,.35) 0%,rgba(0,0,0,0) 20%),
  linear-gradient(90deg,#1e6f26 0%,#3aa543 25%,#2a8a33 47%,#4a4a4a 49%,#c8191e 52%,#e0262b 75%,#8e0d10 100%)}

.verified{left:0;top:910px;width:741px;text-align:center;font:400 13px "Roboto",sans-serif;color:#333}
.badge{top:937px;width:108px;height:43px;background:var(--white);border:1px solid #ddd;box-shadow:0 2px 3px rgba(0,0,0,.08);display:flex;align-items:center;justify-content:center}
.badge i{display:block}
.badge .b1{width:72px;height:30px;background:#1f4f9c}
.badge .b2{width:16px;height:16px;background:#5a9a2a;margin-right:6px}
.badge .b2b{width:68px;height:14px;background:#cfd3d6;border-radius:2px}
.badge .b3{width:34px;height:34px;border-radius:50%;background:radial-gradient(circle,#2d5aa8 55%,#e07a1a 57%)}
.badge .b4{width:30px;height:30px;border-radius:50%;border:2px solid #9a1c2a;margin-right:6px}
.badge .b4b{width:44px;height:12px;background:#d8d8d8;border-radius:2px}

/* footer */
.footer{left:0;top:995px;width:741px;height:112px;background:var(--footer)}
.footer-col{position:absolute;top:13px}
.footer-col h4{font:600 8.5px "Open Sans",sans-serif;color:#f07c22;margin-bottom:4px}
.footer-col a{display:block;font-size:7.5px;color:#ddd;text-decoration:none;line-height:15.5px}
.footer-note{left:0;top:1107px;width:741px;height:60px;background:var(--footer-dark);padding:9px 80px;font-size:7px;line-height:12.5px;color:#8a8a8a}
.footer-bar{left:0;top:1167px;width:741px;height:33px;background:var(--footer-bottom)}
.footer-bar .legal{position:absolute;left:80px;top:12px;font-size:7px;color:#bbb}
.footer-bar .legal b{color:var(--white);font-weight:600}
.social{position:absolute;left:587px;top:8px;display:flex;gap:3px}
.social i{display:block;width:16px;height:16px;border-radius:2px}
</style>
</head>
<body>

<header>
  <div class="brand abs"><span class="brand-mark"></span><span class="brand-name">Marlowe Capital Group</span></div>
  <form class="access abs">
    <h2>PRIVATE ACCESS!</h2>
    <div class="field" style="left:12px">Acc. Number</div>
    <div class="field" style="left:129px">Acc. Password</div>
    <span class="forgot">Forgot Acc.No/Password?</span>
    <span class="login">LOG IN</span>
  </form>
  <nav class="nav abs">
    <a>HOME</a><a>ABOUT US</a><a>INVESTMENTS</a><a>FUNDS</a><a>BROKERAGE</a><a>EXCHANGE</a><a>ACCOUNTS</a><a>CONTACT US</a>
  </nav>
</header>

<section class="hero abs">
  <div class="slide-side slide-left" role="img" aria-label="Hand with pen over financial charts"></div>
  <div class="slide-side slide-right" role="img" aria-label="Business person at a desk"></div>
  <div class="slide-main">
    <div class="slide-photo" role="img" aria-label="City skyline of lit office towers at dusk">
      <div class="caption">
        <h3>FINANCIAL MANAGEMENT</h3>
        <p>Aliquam molestie, mi et imperdiet euismod, dui purus auctor tellus, et interdum lacus lectus et ante.</p>
      </div>
    </div>
  </div>
  <div class="arrows">
    <svg width="20" height="20" viewBox="0 0 20 20"><circle cx="10" cy="10" r="9.5" fill="#f4f4f4" stroke="#bbb"/><path d="M11.5 6 L7.5 10 L11.5 14" stroke="#444" stroke-width="2" fill="none"/></svg>
    <svg width="20" height="20" viewBox="0 0 20 20"><circle cx="10" cy="10" r="9.5" fill="#f4f4f4" stroke="#bbb"/><path d="M8.5 6 L12.5 10 L8.5 14" stroke="#444" stroke-width="2" fill="none"/></svg>
  </div>
</section>

<div class="ticker abs">
  <span style="margin-left:92px" class="up">▲</span>
  <span>GBP/UAH = <b class="up">12.65761 ▲</b></span>
  <span>GBP/UGX = <b class="down">4010.06174 ▼</b></span>
  <span>GBP/USD = <b class="up">1.55817 ▲</b></span>
  <span>GBP/UYU = <b class="up">34.36026 ▲</b></span>
  <span>GBP/VEF = <b class="flat">0</b></span>
  <span>GBP/VUV = <b class="up">151.3</b></span>
</div>

<main>
  <article class="section abs" style="top:379px">
    <div class="section-head"><h2 style="left:386px">Management &amp; Strategy</h2><span class="pointer" style="left:442px"></span></div>
    <p style="left:14px;top:38px">Aliquam molestie, mi et imperdiet euismod, dui purus auctor tellus, et interdum lacus lectus et ante. Sed accumsan sollicitudin sapien, sit amet adipiscing turpis gravida ac. In congue, neque ac lobortis volutpat, libero mauris varius mi, vitae suscipit ipsum ligula vitae risus. Duis aliquam nibh a dui iaculis viverra id a velit. Vivamus egestas risus in magna varius commodo. Sed semper viverra egestas. Etiam pretium porttitor lectus, vel ornare neque porta volutpat. Aenean a nibh eget turpis vehicula tempus ac sed massa. Vestibulum dolor nulla, ultrices ac tincidunt sed, laoreet non est.</p>
    <span class="more" style="left:14px;top:143px">READ MORE &gt;&gt;</span>
    <div class="frame" style="left:346px;top:41px;width:221px;height:117px"><div class="img-charts" role="img" aria-label="Hands with pen and calculator over bar charts"></div></div>
  </article>

  <article class="section abs" style="top:555px">
    <div class="section-head"><h2 style="left:106px">Funds</h2><span class="pointer" style="left:109px"></span></div>
    <p style="left:248px;top:38px">Aliquam molestie, mi et imperdiet euismod, dui purus auctor tellus, et interdum lacus lectus et ante. Sed accumsan sollicitudin sapien, sit amet adipiscing turpis gravida ac. In congue, neque ac lobortis volutpat, libero mauris varius mi, vitae suscipit ipsum ligula vitae risus. Duis aliquam nibh a dui iaculis viverra id a velit. Vivamus egestas risus in magna varius commodo. Sed semper viverra egestas. Etiam pretium porttitor lectus, vel ornare neque porta volutpat. Aenean a nibh eget turpis vehicula tempus ac sed massa. Vestibulum dolor nulla, ultrices ac tincidunt sed, laoreet non est.</p>
    <span class="more" style="left:248px;top:144px">READ MORE &gt;&gt;</span>
    <div class="frame" style="left:13px;top:41px;width:221px;height:117px"><div class="img-market" role="img" aria-label="Blue market figures over a world map"></div></div>
  </article>

  <article class="section abs" style="top:732px">
    <div class="section-head"><h2 style="left:400px">Currency Exchange</h2><span class="pointer" style="left:442px"></span></div>
    <p style="left:14px;top:38px">Aliquam molestie, mi et imperdiet euismod, dui purus auctor tellus, et interdum lacus lectus et ante. Sed accumsan sollicitudin sapien, sit amet adipiscing turpis gravida ac. In congue, neque ac lobortis volutpat, libero mauris varius mi, vitae suscipit ipsum ligula vitae risus. Duis aliquam nibh a dui iaculis viverra id a velit. Vivamus egestas risus in magna varius commodo. Sed semper viverra egestas. Etiam pretium porttitor lectus, vel ornare neque porta volutpat. Aenean a nibh eget turpis vehicula tempus ac sed massa. Vestibulum dolor nulla, ultrices ac tincidunt sed, laoreet non est.</p>
    <span class="more" style="left:14px;top:145px">READ MORE &gt;&gt;</span>
    <div class="frame" style="left:346px;top:43px;width:220px;height:115px"><div class="img-trade" role="img" aria-label="Green buy and red sell keyboard keys"></div></div>
  </article>
</main>

<h3 class="verified abs">Verified &amp; Protected by</h3>
<div class="badge abs" style="left:118px"><i class="b1"></i></div>
<div class="badge abs" style="left:246px"><i class="b2"></i><i class="b2b"></i></div>
<div class="badge abs" style="left:375px"><i class="b3"></i></div>
<div class="badge abs" style="left:503px"><i class="b4"></i><i class="b4b"></i></div>

<footer>
  <div class="footer abs">
    <div class="footer-col" style="left:80px"><h4>ABOUT US</h4><a>History</a><a>Expertize</a><a>Identity</a><a>Strategy</a><a>Contact Us</a></div>
    <div class="footer-col" style="left:167px"><h4>INVESTMENTS</h4><a>History</a><a>Expertize</a><a>Identity</a><a>Strategy</a><a>Contact Us</a></div>
    <div class="footer-col" style="left:271px"><h4>FUNDS</h4><a>History</a><a>Expertize</a><a>Identity</a><a>Strategy</a><a>Contact Us</a></div>
    <div class="footer-col" style="left:360px"><h4>CURRENCY EXCHANGE</h4><a>History</a><a>Expertize</a><a>Identity</a><a>Strategy</a><a>Contact Us</a></div>
    <div class="footer-col" style="left:493px"><h4>BROKERAGE</h4><a>History</a><a>Expertize</a><a>Identity</a><a>Strategy</a><a>Contact Us</a></div>
    <div class="footer-col" style="left:597px"><h4>ACCOUNTS</h4><a>History</a><a>Expertize</a><a>Identity</a><a>Strategy</a><a>Contact Us</a></div>
  </div>
  <p class="footer-note abs">Aliquam molestie, mi et imperdiet euismod, dui purus auctor tellus, et interdum lacus lectus et ante. Sed accumsan sollicitudin sapien, sit amet adipiscing turpis gravida ac. In congue, neque ac lobortis volutpat, libero mauris varius mi, vitae suscipit ipsum ligula vitae risus.Duis aliquam nibh a dui iaculis viverra id a velit. Vivamus egestas risus in magna varius commodo. Sed semper viverra egestas. Etiam pretium porttitor lectus, vel ornare neque porta volutpat.</p>
  <div class="footer-bar abs">
    <span class="legal">Copyright © 2013. <b>KV Group</b>. All Right Reserved &nbsp;|&nbsp; Legal Disclaimer &nbsp;|&nbsp; Privacy Policy</span>
    <div class="social"><i style="background:#3b5b98"></i><i style="background:#3aa6d8"></i><i style="background:#1f6aa5"></i><i style="background:#ef8a1c"></i></div>
  </div>
</footer>

</body>
</html>
```